Vina Ostrava

Ostrava embodies the purity and intensity of Chile’s cold coastal terroir. The sleek white label and bold X logo reflect the stark beauty and unrelenting nature of these extreme winemaking conditions. Crisp, vibrant, and refreshingly bold, Ostrava is a tribute to the wild energy of the Pacific winds and the cool embrace of the coastal valleys—a wine for those who seek purity and perfection in every sip. We would like to have a simple design focusing o the X, we try some option see attach but we are no satisfied is not enaguh eyes catching
Updates

Please create a mysterious, enigmatic label based on the typography and logo attached to the project. We need at least, at the entry level, five varietal products such as Carménère, Cabernet Sauvignon, Merlot, Chardonnay, and Malbec. Later, we would like to add more premium products, like a Reserva, a Special Reserva, or a Limited Edition. The design should be flexible and easily adaptable to accommodate various products while maintaining the same overall aesthetic.

I upload some wines label with printing technic we would like to use on our label, please incorporate this into your design

Project Brief – Large-Scale Brand Label Design
We are developing a new large-scale brand with a structured range of wines. Below are the key design elements and specifications for the labels:

Pinot Noir, Chardonnay, Syrah (Burgundy bottle shape – must include "Special Reserve" on the label)
General Label Guidelines
Year: Only mention "2024" (do not include the word “vintage”).
Capsules: Use standard-colored capsules only (no branding).
Label Design:
Focus on the label itself; bottle and background are irrelevant.
We can consider a wraparound label, but space must be reserved for back-label information.
Please refer to www.corlenti-wines.example for brand coherence. Let us know if further details are needed.

Target Market(s)

peopels who looking for simple design but strinking with the X . THe X could be like a painting brush somehting which make it look artistic

Industry/Entity Type

Wines producer

Font styles to use
Decorative
Script
Other font styles liked:
• the X would be nice if it look like he is Brush from a painter

Colors
0054AA
0677BA
7BADD7
CADEEF
E8F1F8
FFF300
FFF600
FEFA6F
FFFEC7
FFFEE8
EB3D1F
EC4F4E
F09395
F8D3D4
FCEDEE

Requirements
Must have
• We need to indicate the varietals Cabernet Sauvignon, the vintage 2024, the region DO Central Valley
Nice to have
• option on a burgendy bottle for chardonnay and pinot noir and option on bordeau bottle for Cabernet sauvignon and Merlot, We will need a large serie of 5 entrance lebvel (4 red one white) 2 reserve, 2 special reserve, 2 Limited

```html
<!DOCTYPE html>
<html lang="en">
<head>
<meta charset="UTF-8">
<title>Ostrava – Cabernet Sauvignon 2024</title>
<link rel="stylesheet" href="https://fonts.googleapis.com/css2?family=Alegreya+Sans:wght@300;800&display=swap">
<style>
  :root {
    --paper: #ffffff;
    --ink: #0a0a0a;
    --brand-red: #bc181e;
  }
  html, body {
    margin: 0;
    padding: 0;
    width: 1200px;
    height: 720px;
    overflow: hidden;
    background: var(--paper);
  }
  .label {
    position: relative;
    width: 1200px;
    height: 720px;
    background: var(--paper);
    font-family: "Alegreya Sans", sans-serif;
    color: var(--ink);
    font-variant-numeric: lining-nums;
  }
  .brand-name {
    position: absolute;
    left: 0;
    right: 0;
    top: 252px;
    margin: 0;
    text-align: center;
    font-weight: 800;
    font-size: 84px;
    line-height: 1;
    color: var(--brand-red);
    letter-spacing: 1px;
  }
  .varietal {
    position: absolute;
    left: 0;
    right: 0;
    top: 442px;
    margin: 0;
    text-align: center;
    font-weight: 800;
    font-size: 37px;
    line-height: 1;
    letter-spacing: 0.3px;
  }
  .year {
    position: absolute;
    left: 0;
    right: 0;
    top: 482px;
    margin: 0;
    text-align: center;
    font-weight: 300;
    font-size: 28px;
    line-height: 1;
  }
  .appellation {
    position: absolute;
    left: 0;
    right: 0;
    top: 512px;
    margin: 0;
    text-align: center;
    font-weight: 300;
    font-size: 16px;
    line-height: 1;
    letter-spacing: 0.4px;
  }
</style>
</head>
<body>
  <main class="label">
    <p class="brand-name">Ostrava</p>
    <h1 class="varietal">Cabernet Sauvignon</h1>
    <p class="year">2024</p>
    <p class="appellation">DO Central Valley</p>
  </main>
</body>
</html>
```